Webdesign für Anbieter von Wander- und Aktivreisen
Zielgruppe
Wir sind eine Firma in Gründung mit Ziel Wander- und Aktivreisen über die Plattform Pfadkompass.de zu verkaufen. Die Zielgruppe sind aktive Menschen zwischen 25-75 Jahren, die sich gerne aktiv im Urlaub bewegen. Ziel ist eine Plattform aufzubauen um verschiedene aktive Reisen zu vermitteln.
Aufgabenstellung
Das Design soll modern und in Anlehnung an das bereits erstellte Logo Design (siehe Anhang) erstellt werden. Weitere Infos siehe Briefing.

```html
<!DOCTYPE html>
<html lang="de">
<head>
<meta charset="utf-8">
<title>Pfadkompass.de – Wander- und Aktivreisen</title>
<link href="https://fonts.googleapis.com/css2?family=Lato:ital,wght@0,300;0,400;0,700;0,900;1,400&display=swap" rel="stylesheet">
<style>
:root{
  --teal:#0b4656;
  --teal-dark:#073b49;
  --orange:#ff6a00;
  --orange-soft:#ff8a3d;
  --text:#3b4a50;
  --muted:#6d7b80;
  --light:#f4f5f5;
  --btn-grey:#e3ebec;
  --white:#ffffff;
}
*{box-sizing:border-box;margin:0;padding:0}
html,body{width:1200px;height:2775px;overflow:hidden}
body{font-family:"Lato",sans-serif;color:var(--text);background:var(--white);position:relative}
.abs{position:absolute}

/* hero */
.hero{left:0;top:0;width:1200px;height:503px;background:var(--teal)}
.hero-art{left:600px;top:90px;width:450px;height:324px;background:linear-gradient(180deg,#8fb9c3 0%,#b8c3cf 55%,#b99bb2 100%);opacity:.55}
.brand{left:151px;top:18px;display:flex;align-items:center;gap:10px}
.brand-mark{width:14px;height:14px;background:var(--orange)}
.brand-name{font-weight:900;font-size:22px;color:var(--white)}
.contact{right:150px;top:10px;display:flex;gap:26px;font-size:13px;color:var(--white);font-weight:700}
.contact span{display:flex;align-items:center;gap:8px}
.contact .ico{width:22px;height:22px;border-radius:50%;background:var(--orange);display:flex;align-items:center;justify-content:center}
.nav{right:150px;top:50px;display:flex;font-size:13.5px;font-weight:700;color:var(--white)}
.nav a{padding:0 11px 12px;color:inherit;text-decoration:none}
.nav a.active{border-bottom:2px solid var(--orange)}
.headline{left:150px;top:198px;border-left:3px solid var(--orange);padding-left:18px}
.headline .l1{font-weight:300;font-size:40px;color:var(--white);line-height:1.05}
.headline .l2{font-weight:900;font-size:42px;color:var(--btn-grey);line-height:1.1}

.search{left:150px;top:414px;width:900px;height:89px;background:var(--orange);border-radius:4px 4px 0 0}
.field{position:absolute;top:14px}
.field label{display:block;font-size:14px;font-weight:700;color:var(--white);margin-bottom:9px;padding-left:22px}
.select{width:230px;height:33px;background:var(--white);border-radius:2px;font-size:12px;color:var(--text);display:flex;align-items:center;justify-content:space-between;padding:0 14px 0 18px}
.select i{width:0;height:0;border-left:5px solid transparent;border-right:5px solid transparent;border-top:6px solid var(--teal)}
.btn-search{position:absolute;left:738px;top:41px;width:148px;height:33px;background:var(--teal);color:var(--white);font-weight:700;font-size:13px;display:flex;align-items:center;justify-content:center;border-radius:2px}

/* sections */
.sec-title{left:150px;font-size:20px;font-weight:700;color:var(--orange)}
.more{left:933px;width:118px;height:33px;background:var(--btn-grey);border-radius:3px;font-size:12px;font-weight:700;color:var(--teal);display:flex;align-items:center;justify-content:center;gap:8px}
.card{width:288px}
.card .ph{width:288px;height:239px}
.card h3{font-size:15.5px;font-weight:700;color:var(--teal);margin:10px 0 0 -2px}
.card p{font-size:11.5px;color:var(--text);margin:5px 0 0 -2px}
.card .mehr{display:inline-flex;align-items:center;gap:8px;margin:10px 0 0 -2px;border:1px solid #dfe4e5;height:28px;padding:0 18px;font-size:11.5px;font-weight:700;color:var(--orange)}
.card .mehr i{width:0;height:0;border-top:4px solid transparent;border-bottom:4px solid transparent;border-left:5px solid var(--orange)}

/* newsletter */
.news{left:150px;top:1972px;width:900px;height:157px;background:var(--teal);overflow:hidden}
.news-orange{position:absolute;left:0;top:0}
.news h2{position:absolute;left:26px;top:33px;font-size:17.5px;color:var(--white);font-weight:700;line-height:1.3}
.news p{position:absolute;left:27px;top:94px;font-size:11px;color:#a9c2c8;line-height:1.5}
.inp{position:absolute;height:27px;background:var(--white);font-size:11px;color:var(--muted);padding-left:11px;display:flex;align-items:center}
.btn-sub{position:absolute;left:598px;top:97px;width:162px;height:26px;background:var(--teal);color:var(--white);font-size:11px;font-weight:700;display:flex;align-items:center;justify-content:center;gap:6px}

/* reviews */
.rev-title{left:151px;top:2199px;font-size:20px;font-weight:700;color:var(--orange)}
.rev-sub{left:151px;top:2236px;font-size:11.5px;line-height:1.3;color:var(--text)}
.rating{left:912px;top:2195px}
.rating .name{font-size:40px;font-weight:700;color:var(--teal);letter-spacing:-1px;line-height:1}
.rating .lbl{font-size:12px;font-weight:700;color:var(--muted);display:flex;gap:6px;align-items:center}
.stars{color:#f2a81d;letter-spacing:2px}
.review{top:2293px;width:426px;height:278px;background:var(--light);border:1px solid #e5e8e8;padding:44px 47px}
.review .stars{font-size:14px}
.review h4{font-size:13px;color:var(--teal);font-weight:700;margin-top:8px}
.review em{display:block;font-size:11px;color:var(--muted);margin-top:4px}
.review p{font-size:11.5px;color:var(--muted);line-height:1.6;margin-top:18px}
.review .btn{display:inline-flex;width:88px;height:32px;background:var(--teal);color:var(--white);font-size:12px;font-weight:700;align-items:center;justify-content:center;margin-top:24px}
.dots{left:566px;top:2604px;display:flex;gap:8px}
.dots span{width:7px;height:7px;border-radius:50%;background:var(--teal)}
.dots span:first-child{background:var(--orange)}

/* footer */
.footer{left:0;top:2677px;width:1200px;height:98px;background:var(--teal-dark)}
.foot-brand{position:absolute;left:151px;top:36px;font-weight:900;font-size:18px;color:#2f6272}
.social{position:absolute;left:515px;top:42px;display:flex;gap:22px}
.social span{width:14px;height:14px;border-radius:50%;background:#3c6d7b}
.social span:first-child{background:var(--white)}
.foot-links{position:absolute;right:150px;top:42px;font-size:12px;color:#bcd0d5}
</style>
</head>
<body>

<section class="abs hero">
  <div class="abs hero-art" role="img" aria-label="Illustration: zwei Bergsteiger helfen sich gegenseitig auf einen Gipfel vor hellem Bergpanorama"></div>

  <div class="abs brand"><span class="brand-mark"></span><span class="brand-name">Pfadkompass.de</span></div>

  <div class="abs contact">
    <span><span class="ico"><svg width="11" height="11" viewBox="0 0 24 24"><path d="M6.6 10.8a15 15 0 0 0 6.6 6.6l2.2-2.2c.3-.3.7-.4 1-.2 1.1.4 2.3.6 3.6.6.6 0 1 .4 1 1V20c0 .6-.4 1-1 1A17 17 0 0 1 3 4c0-.6.4-1 1-1h3.5c.6 0 1 .4 1 1 0 1.3.2 2.5.6 3.6.1.3 0 .7-.2 1z" fill="#fff"/></svg></span>1800.555.0142</span>
    <span><span class="ico"><svg width="12" height="10" viewBox="0 0 24 18"><rect x="1" y="1" width="22" height="16" fill="none" stroke="#fff" stroke-width="2"/><path d="M1 1l11 9 11-9" fill="none" stroke="#fff" stroke-width="2"/></svg></span>kontakt@pfadkompass.de</span>
  </div>

  <nav class="abs nav">
    <a class="active" href="#">Startseite</a><a href="#">Reise finden</a><a href="#">Reiseziele</a><a href="#">Reisearten</a><a href="#">Informationen</a><a href="#">Kontakt</a>
  </nav>

  <div class="abs headline">
    <div class="l1">Duis aute irure</div>
    <div class="l2">dolor in reprehenderit</div>
  </div>

  <form class="abs search">
    <div class="field" style="left:5px"><label>Reiseziel</label><div class="select" style="margin-left:11px">Auswählen Reiseziel<i></i></div></div>
    <div class="field" style="left:241px"><label>Reiseart</label><div class="select" style="margin-left:11px">Auswählen Reiseart<i></i></div></div>
    <div class="field" style="left:482px"><label>Mit wem reisen sie</label><div class="select" style="margin-left:11px">mit Freunden<i></i></div></div>
    <div class="btn-search">SUCHE</div>
  </form>
</section>

<h2 class="abs sec-title" style="top:570px">Inspiration für einen aktiven Urlaub</h2>
<div class="abs more" style="top:566px">Mehr sehen <span>→</span></div>
<article class="abs card" style="left:150px;top:626px"><div class="ph" role="img" aria-label="Foto: Frau im gelben Kleid vor tropischer Insel" style="background:linear-gradient(160deg,#a9cde6,#3f8a6b 55%,#e0b12a)"></div><h3>Excepteur sint occaecat cupidatat</h3><p>Sunt in culpa qui officia deserunt mollit anim id...</p><span class="mehr"><i></i>Mehr...</span></article>
<article class="abs card" style="left:457px;top:626px"><div class="ph" role="img" aria-label="Foto: Zelt auf einer Bergwiese bei Sonnenuntergang" style="background:linear-gradient(180deg,#f1a94a,#e8c080 40%,#7c9a55)"></div><h3>Excepteur sint occaecat cupidatat</h3><p>Sunt in culpa qui officia deserunt mollit anim id...</p><span class="mehr"><i></i>Mehr...</span></article>
<article class="abs card" style="left:763px;top:626px"><div class="ph" role="img" aria-label="Foto: Wanderer klettert auf einen Felsen" style="background:linear-gradient(180deg,#d7dadb,#b9b3ab 45%,#a3502a)"></div><h3>Excepteur sint occaecat cupidatat</h3><p>Sunt in culpa qui officia deserunt mollit anim id...</p><span class="mehr"><i></i>Mehr...</span></article>

<h2 class="abs sec-title" style="top:1044px">Beliebte Reisen</h2>
<div class="abs more" style="top:1040px">Mehr sehen <span>→</span></div>
<article class="abs card" style="left:150px;top:1100px"><div class="ph" role="img" aria-label="Foto: Wanderer macht ein Selfie vor Bergtal" style="background:linear-gradient(160deg,#5d9fb9,#6d8e7e 50%,#c0702a)"></div><h3>Excepteur sint occaecat cupidatat</h3><p>Sunt in culpa qui officia deserunt mollit anim id...</p><span class="mehr"><i></i>Mehr...</span></article>
<article class="abs card" style="left:457px;top:1100px"><div class="ph" role="img" aria-label="Foto: Freundinnen vor einer Kathedrale" style="background:linear-gradient(180deg,#5a9ed9,#8b8177 45%,#6c5a4c)"></div><h3>Excepteur sint occaecat cupidatat</h3><p>Sunt in culpa qui officia deserunt mollit anim id...</p><span class="mehr"><i></i>Mehr...</span></article>
<article class="abs card" style="left:763px;top:1100px"><div class="ph" role="img" aria-label="Foto: Familie beim Schlittenfahren im Winterwald" style="background:linear-gradient(180deg,#4d5a3c,#8f8f86 50%,#e7ecef)"></div><h3>Excepteur sint occaecat cupidatat</h3><p>Sunt in culpa qui officia deserunt mollit anim id...</p><span class="mehr"><i></i>Mehr...</span></article>

<h2 class="abs sec-title" style="top:1518px">Beliebte Ziele</h2>
<div class="abs more" style="top:1514px">Mehr sehen <span>→</span></div>
<article class="abs card" style="left:150px;top:1574px"><div class="ph" role="img" aria-label="Foto: Liegestühle an einem Sandstrand" style="background:linear-gradient(180deg,#3f8fd0,#9fc6de 40%,#d86a3b 70%,#d9cbb4)"></div><h3>Excepteur sint occaecat cupidatat</h3><p>Sunt in culpa qui officia deserunt mollit anim id...</p><span class="mehr"><i></i>Mehr...</span></article>
<article class="abs card" style="left:457px;top:1574px"><div class="ph" role="img" aria-label="Foto: Steg zu Wasserbungalows über türkisem Meer" style="background:linear-gradient(180deg,#b5cbd6,#2fb3b8 45%,#9c7b5c)"></div><h3>Excepteur sint occaecat cupidatat</h3><p>Sunt in culpa qui officia deserunt mollit anim id...</p><span class="mehr"><i></i>Mehr...</span></article>
<article class="abs card" style="left:763px;top:1574px"><div class="ph" role="img" aria-label="Foto: Bergsee mit Kanus vor Tannenwald" style="background:linear-gradient(180deg,#a5adb0,#2f4d3a 40%,#3aa6b4)"></div><h3>Excepteur sint occaecat cupidatat</h3><p>Sunt in culpa qui officia deserunt mollit anim id...</p><span class="mehr"><i></i>Mehr...</span></article>

<section class="abs news">
  <svg class="news-orange" width="900" height="157" viewBox="0 0 900 157">
    <polygon points="445,0 900,0 900,157 445,157 475,78" fill="var(--orange-soft)"/>
    <polygon points="460,0 900,0 900,157 460,157 490,78" fill="var(--orange)"/>
  </svg>
  <h2>Möchten Sie mit der Trekkingwelt in Kontakt bleiben?<br>Melden Sie sich für unseren beliebten Newsletter an!</h2>
  <p>Wir haben tolle Trekking-Tipps, Trek-Updates und Trek-Gespräche, auf<br>die Sie sich freuen können</p>
  <div class="inp" style="left:512px;top:36px;width:162px">Vorname</div>
  <div class="inp" style="left:683px;top:36px;width:161px">Nachname</div>
  <div class="inp" style="left:512px;top:69px;width:332px">Email</div>
  <div class="btn-sub">→ ABONNIEREN</div>
</section>

<h2 class="abs rev-title">Trekker Geschichten und Erfahrungen mit Pfadkompass</h2>
<p class="abs rev-sub">Über 20.000 Menschen wandern jedes Jahr mit pfadkompass und bürgen für unsere<br>unübertroffenen Sicherheitsstandards. Sehen Sie unten, was sie zu sagen haben.</p>
<div class="abs rating"><div class="name">Rezensio</div><div class="lbl">Bewertungen <span class="stars" style="font-size:10px">★★★★★</span></div></div>

<svg class="abs" style="left:98px;top:2413px" width="22" height="34" viewBox="0 0 22 34"><path d="M18 2L4 17l14 15" fill="none" stroke="var(--teal)" stroke-width="3"/></svg>
<article class="abs review" style="left:150px">
  <div class="stars">★★★★★</div><h4>Advin Dave</h4><em>Excepteur sint occaecat cupidatat non proident</em>
  <p>Ut enim ad minim veniam, quis nostrud exercitation ullamco laboris nisi ut aliquip ex ea commodo consequat. Duis aute irure dolor in reprehenderit in voluptate velit esse cillum dolore eu fugiat nulla pariatur.</p>
  <span class="btn">Mehr...</span>
</article>
<article class="abs review" style="left:623px">
  <div class="stars">★★★★★</div><h4>John Doe</h4><em>Excepteur sint occaecat cupidatat non proident</em>
  <p>Lorem ipsum dolor sit amet, consectetur adipiscing elit, sed do eiusmod tempor incididunt ut labore et dolore magna aliqua. Ut enim ad minim veniam, quis nostrud exercitation ullamco laboris nisi ut aliquip ex ea commodo consequat.</p>
  <span class="btn">Mehr...</span>
</article>
<svg class="abs" style="left:1080px;top:2413px" width="22" height="34" viewBox="0 0 22 34"><path d="M4 2l14 15L4 32" fill="none" stroke="var(--orange)" stroke-width="3"/></svg>
<div class="abs dots"><span></span><span></span><span></span><span></span><span></span></div>

<footer class="abs footer">
  <div class="foot-brand">Pfadkompass.de</div>
  <div class="social"><span></span><span></span><span></span><span></span><span></span></div>
  <div class="foot-links">AGB &nbsp;|&nbsp; Datenschutz &nbsp;|&nbsp; Impressum &nbsp;|&nbsp; Kontakt</div>
</footer>

</body>
</html>
```